Business Cards and Stationery for Mobile Ultrasound
Redfern Harbor Mobile Ultrasound
Business Cards and Stationery for Mobile Ultrasound - Medical
Creative Brief
Professional
Marovic Deltrane
P.O Box 827 Quenton CA 95871
mar@rhqx.example
rhqx.example

```html
<!DOCTYPE html>
<html lang="en">
<head>
<meta charset="utf-8">
<title>Redfern Harbor Mobile Ultrasound – Business Card</title>
<link rel="stylesheet" href="https://fonts.googleapis.com/css2?family=Open+Sans:wght@400;600&display=swap">
<style>
  :root {
    --purple-deep: #3a1466;
    --purple: #5a2a92;
    --purple-light: #7a4cb5;
    --green: #3aa23a;
    --white: #ffffff;
    --backdrop: #e9e8ec;
    --text-light: #f3eefb;
  }
  * { margin: 0; padding: 0; box-sizing: border-box; }
  html, body { width: 1200px; height: 871px; overflow: hidden; }
  body {
    background: var(--backdrop);
    font-family: "Open Sans", Arial, sans-serif;
    position: relative;
  }
  .card {
    position: absolute;
    width: 520px;
    height: 297px;
    border-radius: 14px;
    overflow: hidden;
  }
  .card-back {
    left: 80px;
    top: 170px;
    background: linear-gradient(160deg, var(--purple-light) 0%, var(--purple) 45%, var(--purple-deep) 100%);
  }
  .card-back .brand-name {
    position: absolute;
    left: 0; right: 0; top: 118px;
    text-align: center;
    color: var(--white);
    font-weight: 600;
    font-size: 26px;
    line-height: 1.25;
  }
  .card-front { left: 600px; top: 404px; background: var(--purple); }
  .card-front .card-shape { position: absolute; inset: 0; }
  .card-front .brand-name {
    position: absolute;
    left: 190px; top: 62px; width: 310px;
    text-align: center;
    color: var(--purple);
    font-weight: 600;
    font-size: 26px;
    line-height: 1.2;
  }
  .contact {
    position: absolute;
    left: 22px; top: 142px;
    color: var(--text-light);
    font-size: 11px;
  }
  .contact .person {
    font-size: 15px;
    font-weight: 600;
    margin-bottom: 8px;
  }
  .contact ul { list-style: none; }
  .contact li {
    display: flex; align-items: center; gap: 6px;
    margin-bottom: 5px;
  }
  .contact svg { width: 12px; height: 12px; flex: none; }
  .contact .address { margin-top: 8px; }
</style>
</head>
<body>

<section class="card card-back">
  <p class="brand-name">Redfern Harbor<br>Mobile Ultrasound</p>
</section>

<section class="card card-front">
  <svg class="card-shape" viewBox="0 0 520 297" preserveAspectRatio="none">
    <defs>
      <linearGradient id="front-purple" x1="0" y1="0" x2="0" y2="1">
        <stop offset="0" stop-color="#6a3aa6"/>
        <stop offset="1" stop-color="#3a1466"/>
      </linearGradient>
    </defs>
    <rect width="520" height="297" fill="url(#front-purple)"/>
    <path d="M80,0 C150,150 300,250 520,262 L520,297 L420,297 C290,270 160,180 80,0 Z" fill="#3aa23a"/>
    <path d="M96,0 C170,140 310,235 520,245 L520,0 Z" fill="#ffffff"/>
    <path d="M96,0 C170,140 310,235 520,245" fill="none" stroke="#5a2a92" stroke-width="3"/>
  </svg>

  <p class="brand-name">Redfern Harbor<br>Mobile Ultrasound</p>

  <div class="contact">
    <p class="person">Marovic Deltrane</p>
    <ul>
      <li>
        <svg viewBox="0 0 12 12"><circle cx="6" cy="6" r="6" fill="#fff"/><path d="M4,3 L5,3 L5.5,4.5 L4.8,5 C5.2,6 6,6.8 7,7.2 L7.5,6.5 L9,7 L9,8 C6,8.5 3.5,6 4,3 Z" fill="#5a2a92"/></svg>
        <span>5550142678</span>
      </li>
      <li>
        <svg viewBox="0 0 12 12"><circle cx="6" cy="6" r="6" fill="#fff"/><rect x="3" y="4" width="6" height="4.2" fill="none" stroke="#5a2a92" stroke-width="0.9"/><path d="M3,4 L6,6.4 L9,4" fill="none" stroke="#5a2a92" stroke-width="0.9"/></svg>
        <span>mar@rhqx.example</span>
      </li>
      <li>
        <svg viewBox="0 0 12 12"><circle cx="6" cy="6" r="6" fill="#fff"/><circle cx="6" cy="6" r="3.2" fill="none" stroke="#5a2a92" stroke-width="0.9"/><path d="M2.8,6 L9.2,6 M6,2.8 C4.6,4.5 4.6,7.5 6,9.2 M6,2.8 C7.4,4.5 7.4,7.5 6,9.2" fill="none" stroke="#5a2a92" stroke-width="0.8"/></svg>
        <span>www.rhqx.example</span>
      </li>
    </ul>
    <p class="address">P.O Box 827 Quenton CA 95871</p>
  </div>
</section>

</body>
</html>
```